financial company web page

We are tax and financial consulting company that needs a web site. Our logo is attached. Headquarters of our company is based in Latvia, Riga. Our actual temporary web site is www.norquill.com The main purpose of our new web site is:
* to explain the benefits of doing business through Latvian LLC companies;
* provide necessary information about taxation regime in Latvia for trading and holding companies
* propose some standard schemes of using Latvian companies for various businesses.
* offer our clients other jurisdictions companies - other European, offshore, etc.
* offer our clients ecommerce solutions
* offer our client residency in Latvia and EU
Registration of a Latvian company + accounting + legal advice will be our primary product. However, web site first page should highlight 4 other important products, such as:
1 - eCommerce (here we will explain briefly what is eCommerce, how our client can use it, what are the bonuses doing business online, explain conditions of eCommerce, etc) ;
2 - Residence Permit (here we offer EU and non-EU citizens to obtain Latvian residence permit and explain the benefits of having Latvian ID card);
3 - other Jurisdictions (here we propose list of other companies registered in the countries with favorable taxation regime, i.e. UK, Hong-Kong, Canada, Panama, BVI, UAE, etc);
4 - banking (here we explain benefits of having bank account in Latvia, explaining briefly products that bank offer, etc).
Overall Website map is the following:
1. About us
2. About Latvia
3. Contacts
4. Latvian company
5. Our services
a. еCommerce
b. Resident permit (Latvia and EU)
c. Bank accounts
d. Registration and support of other jurisdictions (European companies, Low tax companies, Offshore companies)
e. Additional services (Tax advisory, Virtual office, European licenses, Accounting services, Legal address in Riga)
6. Become Partner
7. Tembrole Travel Guide
As a start point we need only first page design. If this design suits us well we will continue to work with you on other pages. We are looking for innovative, creative and professional design in line with our corporate logo and colours. We want this design to focus more on graphic, on simplicity and usability. It should be immediately clear from the first glance what the site is about, what is our key product and how to get more information if I'm interested on something.
These are website from our sector, we want to be better:
http://www.vantel-ridge.com/
http://www.qpr-harbourline.com/
http://www.dxlventurebuilders.com/
http://www.firmstarter318.co.uk/
In case you can't find our logo, please, ask I will send it to your mail. Thanks!
Target Market(s)
European, Russian or Chinesee enterpreneurs
Industry/Entity Type
Accounting
Requirements
Must have
- Web site will be on 10 languages, so somewhere must be a button/flag to switch language.
Contact information should be on every page (phone number and add Skype buttons or similar).
Search button should be available on the first page
Button Request a Call should be on every page.
Visitors should also have a possibility to download a brochure about each product (so appropriate button should be in each section).

```html
<!DOCTYPE html>
<html lang="en">
<head>
<meta charset="utf-8">
<title>Tembrole — Tax and financial solutions</title>
<link href="https://fonts.googleapis.com/css2?family=Open+Sans:wght@400;600;700&display=swap" rel="stylesheet">
<style>
:root{
  --navy:#1f2f63;
  --navy-band:#2b3a63;
  --nav-bar:rgba(36,58,120,.95);
  --card-bg:rgba(60,72,110,.78);
  --card-active:rgba(48,58,92,.86);
  --blue-btn:#2f7fc1;
  --link:#2a7fc0;
  --text:#555;
  --text-dark:#444;
  --muted:#999;
  --line:#e2e2e2;
  --white:#fff;
}
*{box-sizing:border-box;margin:0;padding:0}
html,body{width:1200px;height:701px;overflow:hidden;background:var(--white);font-family:"Open Sans",Arial,sans-serif;color:var(--text)}
.page{position:relative;width:1200px;height:701px}

/* header */
.site-header{position:absolute;top:0;left:0;width:1200px;height:75px}
.brand{position:absolute;left:199px;top:19px;display:flex;align-items:center;gap:10px}
.brand-mark{width:32px;height:32px;border-radius:50%;background:var(--navy)}
.brand-name{font-size:30px;font-weight:700;color:var(--navy);line-height:1}
.top-links{position:absolute;left:0;top:0;width:830px;height:75px;font-size:11px;color:var(--text-dark)}
.top-links > *{position:absolute}
.home-ico{left:575px;top:32px}
.about-link{left:591px;top:29px}
.top-links .sep{left:668px;top:32px;width:1px;height:10px;background:#ccc}
.lang-label{left:678px;top:29px}
.flag{left:790px;top:33px;width:13px;height:9px;background:linear-gradient(#9e2a35 0 40%,#fff 40% 60%,#9e2a35 60%)}
.caret{left:814px;top:35px}
.search{position:absolute;left:838px;top:23px;width:173px;height:27px;border:1px solid #d8d8d8}
.search svg{position:absolute;right:8px;top:8px}

/* hero */
.hero{position:absolute;top:75px;left:0;width:1200px;height:437px;
  background:linear-gradient(180deg,#9cc1e8 0%,#c9dcef 28%,#e7edf2 42%,#dfe6ec 55%,#b9b4ad 72%,#8a7a6c 100%)}
.hero-arrow{position:absolute;top:171px;width:42px;height:84px;background:rgba(50,70,120,.45);display:flex;align-items:center;justify-content:center}
.hero-arrow.prev{left:0}
.hero-arrow.next{right:0}
.service-nav{position:absolute;left:197px;top:240px;width:804px;height:47px;background:var(--nav-bar)}
.service-nav a{position:absolute;top:14px;color:var(--white);text-decoration:none;font-size:12.5px;font-weight:600;white-space:nowrap}
.service-nav .collapse{position:absolute;right:30px;top:20px}
.service-cards{position:absolute;left:197px;top:287px;width:804px;height:125px;display:flex}
.card{width:198px;background:var(--card-bg);display:flex;padding:34px 0 0 22px;gap:12px}
.card.active{width:206px;background:var(--card-active)}
.card svg{flex:none}
.card h3{font-size:12.5px;font-weight:600;color:var(--white);margin-bottom:5px;white-space:nowrap}
.card p{font-size:11px;line-height:20px;color:#dfe3ee;white-space:nowrap}

/* band */
.link-band{position:absolute;top:512px;left:0;width:1200px;height:43px;background:var(--navy-band)}
.link-band a{position:absolute;top:14px;font-size:11px;color:var(--white);text-decoration:none}
.request-call{position:absolute;left:897px;top:8px;width:102px;height:25px;background:var(--blue-btn);color:var(--white);font-size:9px;font-weight:600;display:flex;align-items:center;justify-content:center;letter-spacing:.2px}

/* info */
.news{position:absolute;left:196px;top:586px;font-size:10px;line-height:16px}
.news h4{font-size:10px;font-weight:700;color:#666}
.news p{color:var(--text)}
.news a{color:var(--link);text-decoration:none}
.contact-phone{position:absolute;left:594px;top:585px;text-align:right;width:124px}
.contact-phone .num{font-size:15px;color:#666;display:flex;align-items:center;justify-content:flex-end;gap:4px}
.contact-phone .mail{font-size:10px;color:var(--muted)}
.vsep{position:absolute;top:587px;width:1px;height:28px;background:var(--line)}
.call-contact{position:absolute;left:759px;top:585px}
.call-contact .dot{position:absolute;left:0;top:2px;width:16px;height:16px;border-radius:50%;background:var(--link)}
.call-contact b{position:absolute;left:29px;top:0;font-size:12px;font-weight:700;color:#666;white-space:nowrap}
.call-contact span.note{position:absolute;left:29px;top:17px;font-size:10px;color:var(--muted);white-space:nowrap}
.social{position:absolute;left:886px;top:592px;display:flex;gap:15px}
.social i{display:block;width:15px;height:15px;border-radius:50%;background:#c4c4c4}
.divider{position:absolute;left:196px;top:648px;width:805px;height:1px;background:var(--line)}
.copyright{position:absolute;left:196px;top:664px;font-size:10px;color:var(--text)}
.copyright a{color:var(--link);text-decoration:none}
</style>
</head>
<body>
<div class="page">
  <header class="site-header">
    <div class="brand"><span class="brand-mark"></span><span class="brand-name">Tembrole</span></div>
    <nav class="top-links">
      <svg class="home-ico" width="10" height="9" viewBox="0 0 10 9"><path d="M5 0 10 4.5H8.5V9H6V6H4V9H1.5V4.5H0Z" fill="#bbb"/></svg>
      <span class="about-link">About Tembrole</span>
      <span class="sep"></span>
      <span class="lang-label">Choose your language</span>
      <span class="flag"></span>
      <svg class="caret" width="8" height="5" viewBox="0 0 8 5"><path d="M0 0 4 4 8 0" fill="none" stroke="#bbb" stroke-width="1.2"/></svg>
    </nav>
    <div class="search"><svg width="10" height="10" viewBox="0 0 10 10"><circle cx="4" cy="4" r="3" fill="none" stroke="#bbb" stroke-width="1.4"/><path d="M6.3 6.3 9.5 9.5" stroke="#bbb" stroke-width="1.6"/></svg></div>
  </header>

  <section class="hero" role="img" aria-label="Panoramic winter view of Riga with the frozen river, cable bridge and old town spires">
    <div class="hero-arrow prev"><svg width="14" height="30" viewBox="0 0 14 30"><path d="M13 1 1 15 13 29" fill="none" stroke="#fff" stroke-opacity=".8" stroke-width="1.5"/></svg></div>
    <div class="hero-arrow next"><svg width="14" height="30" viewBox="0 0 14 30"><path d="M1 1 13 15 1 29" fill="none" stroke="#fff" stroke-opacity=".8" stroke-width="1.5"/></svg></div>

    <nav class="service-nav">
      <a href="#" style="left:22px">Latvian Company</a>
      <a href="#" style="left:151px">Other Jurisdictions</a>
      <a href="#" style="left:293px">eCommerce</a>
      <a href="#" style="left:398px">Residence Permit</a>
      <a href="#" style="left:530px">Virtual Office</a>
      <svg class="collapse" width="11" height="7" viewBox="0 0 11 7"><path d="M1 6 5.5 1.5 10 6" fill="none" stroke="#fff" stroke-width="2"/></svg>
    </nav>

    <div class="service-cards">
      <div class="card active">
        <svg width="36" height="40" viewBox="0 0 36 40"><rect x="1.5" y="1.5" width="33" height="22" rx="3" fill="none" stroke="#fff" stroke-width="3"/><rect x="1.5" y="7" width="33" height="4" fill="#fff"/><path d="M12 16h12v16l-4 6h-6l-3-5z" fill="#fff"/></svg>
        <div><h3>eCommece Solution</h3><p>Lorem ipsum dolor sit<br>amet adipiscing elit.</p></div>
      </div>
      <div class="card">
        <svg width="34" height="32" viewBox="0 0 34 32"><path d="M17 1 33 15h-4v16H5V15H1Z" fill="#fff"/><rect x="13" y="19" width="8" height="12" fill="#3c486e"/></svg>
        <div><h3>Residence Permit</h3><p>Lorem ipsum dolor sit<br>amet adipiscing elit.</p></div>
      </div>
      <div class="card">
        <svg width="38" height="28" viewBox="0 0 38 28"><rect x="5" y="1.5" width="31" height="24" fill="none" stroke="#fff" stroke-width="3"/><path d="M1.5 5v21h4" fill="none" stroke="#fff" stroke-width="2.5"/><rect x="10" y="7" width="9" height="7" fill="#fff"/><path d="M22 8h9M22 12h9M10 18h21" stroke="#fff" stroke-width="2"/></svg>
        <div><h3>Other Jurisdictions</h3><p>Lorem ipsum dolor sit<br>amet adipiscing elit.</p></div>
      </div>
      <div class="card">
        <svg width="28" height="34" viewBox="0 0 28 34"><path d="M2 4h14v30H2zM16 12h10v22H16z" fill="#fff"/><g fill="#3c486e"><rect x="5" y="8" width="3" height="3"/><rect x="10" y="8" width="3" height="3"/><rect x="5" y="14" width="3" height="3"/><rect x="10" y="14" width="3" height="3"/><rect x="5" y="20" width="3" height="3"/><rect x="10" y="20" width="3" height="3"/><rect x="19" y="16" width="4" height="3"/><rect x="19" y="22" width="4" height="3"/><rect x="7" y="27" width="4" height="7"/></g></svg>
        <div><h3>Banking</h3><p>Lorem ipsum dolor sit<br>amet adipiscing elit.</p></div>
      </div>
    </div>
  </section>

  <div class="link-band">
    <a href="#" style="left:197px">Become a Partner</a>
    <a href="#" style="left:308px">Sitemap</a>
    <span class="request-call">REQUEST A CALL</span>
  </div>

  <div class="news">
    <h4>What's New at Tembrole</h4>
    <p>New Services of Daugmala Bank for More Convenient Account</p>
    <a href="#">Readmore</a>
  </div>

  <div class="contact-phone">
    <div class="num"><svg width="12" height="13" viewBox="0 0 12 13"><path d="M2 0 4.5 3 3 5c1 2 2.5 3.5 4.5 4.5L9 8l3 2.5-2 2.5C5 12.5 0 7 0 2Z" fill="#777"/></svg>+371 20417736</div>
    <div class="mail">info@tembrole.com</div>
  </div>
  <span class="vsep" style="left:742px"></span>
  <div class="call-contact"><span class="dot"></span><b>tembrole</b><span class="note">for call inly</span></div>
  <span class="vsep" style="left:863px"></span>
  <div class="social"><i></i><i></i><i></i><i></i></div>

  <div class="divider"></div>
  <p class="copyright">© 2013 <a href="#">Tembrole.com</a>&nbsp; Tax and financial solutions. All right reserved &nbsp;|&nbsp; Kalnciema street 12-5, Riga, LV-1011, Latvia</p>
</div>
</body>
</html>
```